Trade Show Booth Sign Design for Retracting Banner

I need a trade show booth sign designed. It will be for a retractable banner that is double sided with 34 by 81 inch.

I want to incorporate my logo (see attached, have it in other file formats as well) and graphics from my website (https://www.pellacorvaadvisory.com/) with parts or all of the following text.

· Educational Content Creation
o Supplemental Textbook Content Development
o E-learning Content Development
· Curriculum Development
o VKTR/Joint Pillar
o Three Dimensional Learning
· Assessment
o Formative Assessments
o Elementary School, Middle School, High School, College, and Business
· Professional Development
o Training
o Facilitation

Target Market(s)

Education

Industry/Entity Type

Education

Font styles to use
Sans Serif

Colors

Designer to choose colors to be used in the design.

Requirements
Must have
• Eye catching and easy to read design
Nice to have
• Would like to see incorporation of my logo and some of the elements of my website images
Should not have
• N/A

```html
<!DOCTYPE html>
<html lang="en">
<head>
<meta charset="utf-8">
<title>Pella Corva Advisory – Our Services</title>
<link rel="stylesheet" href="https://fonts.googleapis.com/css2?family=Roboto:wght@400;700;900&display=swap">
<style>
  :root {
    --navy: #1d2a5c;
    --blue: #2f7fc0;
    --teal: #8fd3da;
    --green: #b8dc8e;
    --lavender: #dccbe6;
    --orange: #f9b34a;
    --board: #2b2c2e;
    --board-light: #4a4b4e;
    --white: #ffffff;
  }
  * { box-sizing: border-box; margin: 0; padding: 0; }
  html, body { width: 1200px; height: 2855px; overflow: hidden; background: var(--white); }
  body { font-family: "Roboto", Arial, sans-serif; color: var(--navy); position: relative; }

  .brand {
    position: absolute; left: 0; top: 40px; width: 1200px;
    text-align: center; font-weight: 900; color: var(--navy); line-height: 1;
  }
  .brand-main { display: block; font-size: 230px; letter-spacing: -4px; }
  .brand-sub { display: block; font-size: 92px; margin-top: 14px; letter-spacing: 2px; }

  .photo-band {
    position: absolute; left: 0; width: 1200px; height: 300px;
    background: radial-gradient(ellipse at 50% 50%, var(--board-light), var(--board) 70%);
  }
  .photo-band.top { top: 470px; }
  .photo-band.bottom { top: 2565px; height: 290px; }

  .section-title {
    position: absolute; left: 0; top: 820px; width: 1200px; text-align: center;
    font-weight: 900; font-size: 138px; color: var(--blue); letter-spacing: 2px; line-height: 1;
  }

  .service {
    position: absolute; padding: 40px 30px 30px 40px;
  }
  .service.content { left: 78px; top: 1000px; width: 507px; height: 745px; background: var(--teal); }
  .service.assessment { left: 608px; top: 1000px; width: 507px; height: 745px; background: var(--green); }
  .service.curriculum { left: 78px; top: 1770px; width: 507px; height: 620px; background: var(--lavender); }
  .service.professional { left: 608px; top: 1770px; width: 507px; height: 620px; background: var(--orange); }

  .service-icon { display: block; margin: 0 auto 28px; width: 190px; height: 140px; }
  .service-heading {
    font-weight: 900; font-size: 56px; line-height: 1.12; text-transform: uppercase;
    color: var(--navy); margin-bottom: 22px; letter-spacing: 0.5px;
  }
  .service-list { list-style: none; }
  .service-list li {
    display: flex; align-items: flex-start; gap: 16px;
    font-size: 40px; line-height: 1.1; margin-bottom: 20px;
  }
  .tick { flex: 0 0 56px; width: 56px; height: 56px; margin-top: -4px; }

  .site-url {
    position: absolute; left: 0; top: 2448px; width: 1200px; text-align: center;
    font-weight: 700; font-size: 58px; color: var(--navy); letter-spacing: 1px;
  }
</style>
</head>
<body>
  <svg width="0" height="0" style="position:absolute">
    <defs>
      <symbol id="tick-box" viewBox="0 0 56 56">
        <rect x="3" y="10" width="40" height="40" fill="none" stroke="#1d2a5c" stroke-width="5"/>
        <path d="M11 28 L22 40 L52 6" fill="none" stroke="#1d2a5c" stroke-width="8" stroke-linecap="square"/>
      </symbol>
    </defs>
  </svg>

  <header class="brand">
    <span class="brand-main">PELLA CORVA</span>
    <span class="brand-sub">ADVISORY</span>
  </header>

  <div class="photo-band top" role="img" aria-label="Chalkboard with hanging light bulbs topped by colourful crumpled paper balls"></div>

  <h1 class="section-title">OUR SERVICES</h1>

  <section class="service content">
    <svg class="service-icon" viewBox="0 0 190 140" fill="none" stroke="#1d2a5c" stroke-width="5">
      <path d="M95 25 C70 10 40 10 20 18 V120 C40 112 70 112 95 127 C120 112 150 112 170 120 V18 C150 10 120 10 95 25 Z"/>
      <path d="M95 25 V127"/>
      <path d="M10 28 V130 C40 122 70 124 95 134 C120 124 150 122 180 130 V28"/>
    </svg>
    <h2 class="service-heading">Educational<br>Content<br>Creation</h2>
    <ul class="service-list">
      <li><svg class="tick"><use href="#tick-box"/></svg><span>Supplemental Textbook</span></li>
      <li><svg class="tick"><use href="#tick-box"/></svg><span>Content Development</span></li>
      <li><svg class="tick"><use href="#tick-box"/></svg><span>E-learning Content Development</span></li>
    </ul>
  </section>

  <section class="service assessment">
    <svg class="service-icon" viewBox="0 0 190 140" fill="none" stroke="#1d2a5c" stroke-width="5">
      <rect x="45" y="10" width="100" height="122"/>
      <path d="M62 40 H110 M62 62 H128 M62 84 H128 M62 106 H110"/>
      <path d="M120 76 L165 18 L178 28 L133 86 L116 92 Z"/>
    </svg>
    <h2 class="service-heading">Assessment</h2>
    <ul class="service-list">
      <li><svg class="tick"><use href="#tick-box"/></svg><span>Formative Assessments</span></li>
      <li><svg class="tick"><use href="#tick-box"/></svg><span>Elementary School, Middle School, High School, College &amp; Business</span></li>
    </ul>
  </section>

  <section class="service curriculum">
    <svg class="service-icon" viewBox="0 0 190 140" fill="none" stroke="#1d2a5c" stroke-width="5">
      <rect x="20" y="30" width="150" height="100" rx="10"/>
      <path d="M30 48 H160"/>
      <path d="M100 100 L150 12 L164 20 L114 108 L98 114 Z"/>
    </svg>
    <h2 class="service-heading">Curriculum<br>Development</h2>
    <ul class="service-list">
      <li><svg class="tick"><use href="#tick-box"/></svg><span>VKTR/Joint Pillar</span></li>
      <li><svg class="tick"><use href="#tick-box"/></svg><span>Three Dimensional Learning</span></li>
    </ul>
  </section>

  <section class="service professional">
    <svg class="service-icon" viewBox="0 0 190 140" fill="none" stroke="#1d2a5c" stroke-width="5">
      <path d="M95 20 L180 55 L95 90 L10 55 Z"/>
      <path d="M45 70 V110 C70 128 120 128 145 110 V70"/>
      <path d="M165 62 V105"/>
      <circle cx="165" cy="110" r="6" fill="#1d2a5c"/>
    </svg>
    <h2 class="service-heading">Professional<br>Development</h2>
    <ul class="service-list">
      <li><svg class="tick"><use href="#tick-box"/></svg><span>Training</span></li>
      <li><svg class="tick"><use href="#tick-box"/></svg><span>Facilitation</span></li>
    </ul>
  </section>

  <p class="site-url">www.pellacorvaadvisory.com</p>

  <div class="photo-band bottom" role="img" aria-label="Chalkboard with light bulbs topped by colourful crumpled paper balls"></div>
</body>
</html>
```